Hedge fund needs power point design for marketing pitch

We need a designer to make our power point pitch more aesthetically appealing to potential clients. We will be marketing our hedge fund to high net worth individuals and financial institutions. The ideal design will look professional and project confidence to our potential clients. We have attached a rough outline of what we have completed so far. We have also attached example cover pages for 2 pitch books produced by our competitors.

Target Market(s)

Financial institutions and wealthy investors

Industry/Entity Type

Finance

Requirements
Must have
• must use our logo and current slides. Must look professional

```html
<!DOCTYPE html>
<html lang="en">
<head>
<meta charset="utf-8">
<title>Fund Pitch Slides</title>
<link rel="stylesheet" href="https://fonts.googleapis.com/css2?family=Cabin:wght@400;500&family=Carlito:wght@400;700&display=swap">
<style>
:root{
  --page:#eef0f2;
  --slide-top:#e6edf5;
  --slide-bottom:#f6f8fb;
  --gold:#c89a2c;
  --gold-light:#e9c33f;
  --gold-dark:#a77e1f;
  --forest:#123a2a;
  --ink:#1b1b1b;
  --red:#e0221f;
  --white:#ffffff;
}
*{box-sizing:border-box;margin:0;padding:0}
html,body{width:1200px;height:1200px;overflow:hidden}
body{background:var(--page);font-family:"Cabin",sans-serif;color:var(--ink);position:relative}
.slide{position:absolute;overflow:hidden;background:linear-gradient(180deg,var(--slide-top),var(--slide-bottom));box-shadow:3px 4px 8px rgba(0,0,0,.35)}
.slide__backdrop{position:absolute;inset:0;background:linear-gradient(120deg,rgba(255,255,255,0) 40%,rgba(190,205,220,.45) 60%,rgba(255,255,255,.1) 80%)}
.slide__footer{position:absolute;left:0;right:0;height:29px;bottom:9px;background:linear-gradient(90deg,var(--gold-dark),var(--gold) 25%,var(--gold-light) 50%,var(--gold) 75%,var(--gold-dark))}
.slide__base{position:absolute;left:0;right:0;bottom:0;height:9px;background:var(--forest)}
.header-band{position:absolute;left:0;background:var(--gold);color:var(--white);border-top:2px solid var(--gold-light);border-right:2px solid var(--gold-light);border-bottom:2px solid var(--gold-light)}
.header-band--small{top:27px;height:37px;font-size:13.5px;display:flex;align-items:center;padding-left:32px}
.header-band--large{top:26px;height:51px;width:378px;font-size:32px;display:flex;align-items:center;padding-left:32px;letter-spacing:.2px}
.sim-slide{top:122px;height:419px}
.sim-slide--avg{left:22px;width:551px}
.sim-slide--cons{left:608px;width:557px}
.chart{position:absolute;top:82px;left:44px;width:198px;height:142px;background:var(--white)}
.sim-slide--cons .chart{left:40px;top:80px;width:200px}
.facts{position:absolute;top:96px;left:270px;width:270px;font-size:10px;line-height:12.6px;list-style:none}
.sim-slide--cons .facts{left:276px;top:98px}
.facts li{position:relative;padding-left:18px}
.facts li::before{content:"•";position:absolute;left:0}
.perf-table{position:absolute;top:242px;left:14px;width:521px;font-family:"Carlito",sans-serif;font-size:6.5px}
.sim-slide--cons .perf-table{left:13px;width:532px}
.perf-table table{width:100%;border-collapse:collapse;table-layout:fixed;background:var(--white)}
.perf-table th{background:var(--forest);color:var(--white);font-weight:700;height:10px}
.perf-table td{text-align:right;padding-right:3px;border:1px solid #cfcfcf;height:10px}
.perf-table td.period{text-align:center;font-weight:700}
.perf-table .neg,.perf-table .hl{color:var(--red)}
.perf-table .note{background:var(--gold);color:var(--white);padding:1px 2px 2px;line-height:11px;font-size:7px}
.perf-table .note b{font-weight:700}
.brand{position:absolute;top:14px;width:92px;text-align:center;font-size:10.5px;letter-spacing:.8px;color:var(--forest);line-height:1.1}
.brand small{display:block;font-size:5.5px;letter-spacing:.3px}
.brand__mark{display:block;width:8px;height:8px;background:var(--forest);margin:0 auto 4px}
.text-slide{top:582px;height:408px}
.text-slide--actual{left:30px;width:548px}
.text-slide--risk{left:619px;width:546px}
.text-slide .brand{left:444px}
.text-slide--risk .brand{left:442px}
.big-list{position:absolute;left:33px;list-style:none}
.big-list li{position:relative;padding-left:20px}
.big-list li::before{content:"•";position:absolute;left:0}
.text-slide--actual .big-list{top:95px;width:360px;font-size:19.5px;line-height:23px}
.text-slide--risk .big-list{top:96px;width:490px;font-size:21px;line-height:20.5px}
.text-slide--risk .big-list li{margin-bottom:5px}
.coins{position:absolute;left:178px;top:165px;width:370px;height:205px;background:radial-gradient(ellipse at 40% 65%,#c9a96a 0%,#d9c7a0 35%,rgba(230,232,235,0) 70%)}
</style>
</head>
<body>

<section class="slide sim-slide sim-slide--avg">
  <div class="slide__backdrop" role="img" aria-label="Faint photo of glass office towers"></div>
  <div class="header-band header-band--small" style="width:491px">Simulated Performance – under our average price discount/premium (8%)</div>
  <svg class="chart" viewBox="0 0 198 142" aria-label="Density chart of simulated monthly, quarterly and annual returns">
    <g stroke="#333" stroke-width=".5" fill="none">
      <line x1="18" y1="8" x2="18" y2="100"/><line x1="18" y1="100" x2="180" y2="100"/><line x1="180" y1="8" x2="180" y2="100"/>
      <path d="M18 100 C26 90 30 10 34 10 C39 10 42 80 52 95 C60 100 90 100 180 100"/>
      <path d="M18 100 C30 80 40 50 46 50 C54 50 60 90 80 98 C100 100 140 100 180 100" stroke-dasharray="2 1.5"/>
      <path d="M18 100 C40 85 60 40 85 20 C100 8 140 8 160 12 C170 16 178 22 180 25" stroke-dasharray=".8 1"/>
      <rect x="57" y="116" width="106" height="18" stroke="#777"/>
      <line x1="62" y1="122" x2="82" y2="122"/><line x1="112" y1="122" x2="130" y2="122" stroke-dasharray="2 1.5"/><line x1="62" y1="129" x2="82" y2="129" stroke-dasharray=".8 1"/>
    </g>
    <g font-size="4.5" fill="#333" font-family="Carlito,sans-serif">
      <text x="86" y="124">monthly</text><text x="133" y="124">quarterly</text><text x="86" y="131">annual</text>
      <text x="88" y="110">% return</text><text x="10" y="102">0</text><text x="10" y="55">.01</text><text x="10" y="12">.03</text>
    </g>
  </svg>
  <ul class="facts">
    <li>Mean simulated annual return is 302%</li>
    <li>Only 1% of simulated annual returns are lower than 25.7%</li>
    <li>The mean 3-year and 5-year simulated returns are 6,109% and 96,093%.</li>
    <li>The worst simulated 3-year return out of 10,000 simulated observations is +88%.</li>
    <li>The worst simulated 5-year return out of 10,000 simulated observations is +1,048%.</li>
  </ul>
  <div class="perf-table">
    <table>
      <tr><th colspan="5"></th><th colspan="4" style="text-align:left">Percentiles</th><th colspan="4"></th></tr>
      <tr><th>period</th><th>mean</th><th>1%</th><th>10%</th><th>25%</th><th>50%</th><th>75%</th><th>90%</th><th>99%</th><th>min</th><th>max</th><th>%+</th></tr>
      <tr><td class="period">monthly</td><td class="hl">11.3</td><td>(13.0)</td><td>(5.7)</td><td>0.2</td><td class="hl">8.6</td><td>19.4</td><td>31.6</td><td>58.5</td><td>(19.3)</td><td>118.8</td><td class="hl">76%</td></tr>
      <tr><td class="period">quarterly</td><td class="hl">37.4</td><td>(15.5)</td><td>1.2</td><td>13.8</td><td class="hl">31.8</td><td>55.1</td><td>80.5</td><td>137.7</td><td>(28.5)</td><td>292.2</td><td class="hl">91%</td></tr>
      <tr><td class="period">1 year</td><td class="hl">302.0</td><td class="hl">25.7</td><td>96.1</td><td>155.1</td><td class="hl">251.8</td><td>394.1</td><td>563.2</td><td>1,040.7</td><td class="hl">(27.7)</td><td>2,251.7</td><td class="hl">99.8%</td></tr>
      <tr><td class="period">3 year</td><td class="hl">6,109.3</td><td class="hl">634.2</td><td>1,511.5</td><td>2,455.8</td><td class="hl">4,291.1</td><td>7,576.9</td><td>12,373.8</td><td>31,693.1</td><td class="hl">88.4</td><td>85,014.2</td><td class="hl">100%</td></tr>
      <tr><td class="period">5 year</td><td class="hl">96,093.4</td><td class="hl">5,128.6</td><td>14,450.8</td><td>27,087.3</td><td class="hl">54,222.7</td><td>112,032.5</td><td>212,569.1</td><td>660,578.3</td><td class="hl">1,047.8</td><td>2,173,490.8</td><td class="hl">100%</td></tr>
      <tr><td class="note" colspan="12" style="text-align:left">Assumes 8% price discount per trade and liquid markets. The table shows returns expressed as a percentage of the initial investment, by the amount of time since the investment period began. Each row shows estimated returns distributions using Monte Carlo simulation and bootstrapping methods. The estimates are drawn from simulated samples containing 10,000 observations for each return. <b>The simulated returns do not account for fees and taxes, which may reduce an investor's actual returns.</b></td></tr>
    </table>
  </div>
  <div class="slide__footer"></div><div class="slide__base"></div>
</section>

<section class="slide sim-slide sim-slide--cons">
  <div class="slide__backdrop" role="img" aria-label="Faint photo of glass office towers"></div>
  <div class="header-band header-band--small" style="width:548px;top:23px;padding-left:32px">Simulated Performance – under a more conservative assumed price discount/premium (5%)</div>
  <svg class="chart" viewBox="0 0 198 142" aria-label="Density chart of simulated monthly, quarterly and annual returns">
    <g stroke="#333" stroke-width=".5" fill="none">
      <line x1="18" y1="8" x2="18" y2="100"/><line x1="18" y1="100" x2="180" y2="100"/><line x1="180" y1="8" x2="180" y2="100"/>
      <path d="M18 100 C24 90 28 12 32 12 C37 12 40 80 50 95 C60 100 90 100 180 100"/>
      <path d="M18 100 C28 70 34 30 38 30 C46 30 50 88 66 98 C90 100 140 100 180 100" stroke-dasharray="2 1.5"/>
      <path d="M18 100 C30 60 40 15 52 15 C70 15 100 60 130 85 C150 97 170 99 180 100" stroke-dasharray=".8 1"/>
      <rect x="57" y="116" width="106" height="18" stroke="#777"/>
      <line x1="62" y1="122" x2="82" y2="122"/><line x1="112" y1="122" x2="130" y2="122" stroke-dasharray="2 1.5"/><line x1="62" y1="129" x2="82" y2="129" stroke-dasharray=".8 1"/>
    </g>
    <g font-size="4.5" fill="#333" font-family="Carlito,sans-serif">
      <text x="86" y="124">monthly</text><text x="133" y="124">quarterly</text><text x="86" y="131">annual</text>
      <text x="88" y="110">% return</text><text x="10" y="102">0</text><text x="10" y="55">.01</text><text x="10" y="12">.03</text>
    </g>
  </svg>
  <ul class="facts">
    <li>Mean simulated annual return is 129%</li>
    <li>1% of the time, annual simulated returns are lower than -29.5%</li>
    <li>The mean 3-year and 5-year simulated returns are 1,129% and 6,759%.</li>
    <li>Only 1% of 5-year returns fall below +216%</li>
    <li>The worst simulated 5-year return out of 10,000 simulated observations is -16%.</li>
  </ul>
  <div class="perf-table">
    <table>
      <tr><th colspan="5"></th><th colspan="4" style="text-align:left">Percentiles</th><th colspan="4"></th></tr>
      <tr><th>period</th><th>mean</th><th>1%</th><th>10%</th><th>25%</th><th>50%</th><th>75%</th><th>90%</th><th>99%</th><th>min</th><th>max</th><th>%+</th></tr>
      <tr><td class="period">monthly</td><td>6.7</td><td>(17.4)</td><td>(10.0)</td><td>(4.0)</td><td>4.3</td><td>15.1</td><td>26.2</td><td>51.8</td><td>(22.7)</td><td>100.0</td><td>63%</td></tr>
      <tr><td class="period">quarterly</td><td class="hl">21.6</td><td>(25.7)</td><td>(10.9)</td><td>0.6</td><td class="hl">16.9</td><td>37.1</td><td>59.9</td><td>114.1</td><td>(37.8)</td><td>200.8</td><td class="hl">76%</td></tr>
      <tr><td class="period">1 year</td><td class="hl">129.2</td><td class="hl">(29.5)</td><td>12.2</td><td>46.7</td><td class="hl">100.3</td><td>178.0</td><td>280.4</td><td>555.1</td><td>(62.1)</td><td>1,403.4</td><td class="hl">94%</td></tr>
      <tr><td class="period">3 year</td><td class="hl">1,129.3</td><td class="hl">37.1</td><td>198.8</td><td>390.7</td><td class="hl">750.0</td><td>1,408.6</td><td>2,436.3</td><td>6,122.8</td><td>(67.0)</td><td>21,804.0</td><td class="hl">99.7%</td></tr>
      <tr><td class="period">5 year</td><td class="hl">6,759.0</td><td class="hl">216.5</td><td>816.4</td><td>1,636.4</td><td class="hl">3,523.6</td><td>7,368.2</td><td>14,846.8</td><td>52,779.2</td><td class="hl">(15.9)</td><td>260,998.3</td><td class="hl">99.97%</td></tr>
      <tr><td class="note" colspan="12" style="text-align:left">Assumes 5% price discount per trade and liquid markets. The table shows returns expressed as a percentage of the initial investment, by the amount of time since the investment period began. Each row shows estimated returns distributions using Monte Carlo simulation and bootstrapping methods. The estimates are drawn from simulated samples containing 10,000 observations for each return. <b>The simulated returns do not account for fees and taxes, which may reduce an investor's actual returns.</b></td></tr>
    </table>
  </div>
  <div class="slide__footer"></div><div class="slide__base"></div>
</section>

<section class="slide text-slide text-slide--actual">
  <div class="slide__backdrop" role="img" aria-label="Faint photo of glass office towers"></div>
  <div class="header-band header-band--large">Actual Performance</div>
  <div class="brand"><span class="brand__mark"></span>ALDER RIDGE<small>CAPITAL MANAGEMENT LLC</small></div>
  <ul class="big-list">
    <li>The fund will launch in May 2016.</li>
    <li>We will report fund performance on a monthly basis starting in June.</li>
  </ul>
  <div class="coins" role="img" aria-label="Photo of rising stacks of gold coins"></div>
  <div class="slide__footer"></div><div class="slide__base"></div>
</section>

<section class="slide text-slide text-slide--risk">
  <div class="slide__backdrop" role="img" aria-label="Faint photo of glass office towers"></div>
  <div class="header-band header-band--large" style="width:378px">Risk Management</div>
  <div class="brand"><span class="brand__mark"></span>ALDER RIDGE<small>CAPITAL MANAGEMENT LLC</small></div>
  <ul class="big-list">
    <li>Our top priority is safety</li>
    <li>If the market does not offer a price discount or premium, we trade at the best available price to stay within our trading parameters.</li>
    <li>This approach minimizes losses in illiquid markets.</li>
    <li>The simulated strategy performance at substantially lower average price discount/ premium, relative to the average we have achieved to date, exhibits limited downside risk (see simulation results at 5% versus 8% discount/premium)</li>
  </ul>
  <div class="slide__footer"></div><div class="slide__base"></div>
</section>

</body>
</html>
```